New Signage Design Project for Qb Dale Outworks *

Im Looking for yard design with our logo, number, website, services & credentials. Each Yard sign will be for 3 different titles...

Example 1: New Roof Coming Soon (Title) This Yardsign is for projects before we start them... Letting neighbors know why we are going to be there.
Example 2: New Roof In progress (Title) This Yardsign is for during the process of the work.. letting neighbors know what we working on!!
Example 3: This Design is only for the customer that says a title NEW ROOF INSTALL SATISFIED CUSTOMER ON THIS DESIGN I DONT NEED SERVICES JSUT LOGO AND THE TITLE

Target Market(s)

Customers

Industry/Entity Type

Roofing

Font styles to use
Serif
Sans Serif

Colors
33b8a4
5c5c5c

Requirements
Must have
• -LOGO
• -WEBSITE
• -NUMBER
• -TITLES
• -SERVICES (ROOFING, GUTTERS, PAINTING, PRESSURE WASHING, EXTERIOR DESIGN.)
• -CREDENTIALS
• -HOUSE SHAPE DESIGN
• -LOGO COLORS
• -NOT BUSY BUT CLEAN AND SHARP
• -MATTE COLORS
Nice to have
• Easy To read, Eye Catchy, Clean Design, logo colors, titles
Should not have
• not Busy,

```html
<!DOCTYPE html>
<html lang="en">
<head>
<meta charset="utf-8">
<title>Qb Dale Outworks – New Roof In Progress Yard Sign</title>
<link rel="stylesheet" href="https://fonts.googleapis.com/css2?family=Source+Sans+3:wght@300;400;600;700&display=swap">
<style>
  :root {
    --teal: #1b9a8c;
    --teal-bright: #33b8a4;
    --charcoal: #5c5c5c;
    --ink: #0b0b0b;
    --paper: #ffffff;
    --backdrop: #e9ebea;
    --text-dark: #2b2b2b;
    --badge-red: #c8342c;
    --badge-blue: #1f4f8f;
  }
  * { box-sizing: border-box; margin: 0; padding: 0; }
  html, body { width: 1200px; height: 821px; overflow: hidden; }
  body {
    background: var(--backdrop);
    font-family: "Source Sans 3", Arial, sans-serif;
    position: relative;
  }
  .yard-sign {
    position: absolute;
    left: 307px; top: 20px;
    width: 585px; height: 780px;
    background: var(--paper);
    overflow: hidden;
    box-shadow: 0 4px 18px rgba(0,0,0,.18);
  }
  .roof-header { position: absolute; left: 0; top: 0; width: 585px; height: 215px; }
  .brand {
    position: absolute; left: 40px; top: 70px;
    display: flex; align-items: center; gap: 10px;
  }
  .brand-mark { width: 22px; height: 22px; background: var(--teal-bright); }
  .brand-name {
    font-weight: 700; font-size: 21px; letter-spacing: .5px;
    color: var(--teal-bright); text-transform: uppercase;
  }
  .title-small {
    position: absolute; left: 0; right: 0; top: 200px; padding-left: 10px;
    text-align: center; font-weight: 300; font-size: 66px; line-height: 1;
    color: var(--charcoal);
  }
  .title-large {
    position: absolute; left: 0; right: 0; top: 274px; padding-left: 10px;
    text-align: center; font-weight: 700; font-size: 70px; line-height: 1;
    color: var(--teal); letter-spacing: -.5px;
  }
  .services-band {
    position: absolute; left: 0; top: 378px; width: 100%; height: 47px;
    background: var(--teal);
    display: flex; justify-content: space-between; align-items: center;
    padding: 0 48px 0 50px;
    color: var(--paper); font-size: 40px; font-weight: 400; line-height: 1;
  }
  .service-list { position: absolute; left: 0; width: 100%; display: flex; list-style: none; }
  .service-list li {
    display: flex; align-items: center; gap: 12px;
    font-size: 23px; color: var(--text-dark);
  }
  .service-list svg { width: 17px; height: 17px; flex: none; }
  .row-one { top: 452px; padding-left: 58px; }
  .row-one li:nth-child(1) { width: 181px; }
  .row-one li:nth-child(2) { width: 179px; }
  .row-two { top: 497px; padding-left: 62px; }
  .row-two li:nth-child(1) { width: 278px; }
  .phone-banner { position: absolute; left: 16px; top: 552px; width: 553px; height: 80px; }
  .phone-number {
    position: absolute; left: 138px; top: 560px;
    font-weight: 700; font-size: 54px; line-height: 1; color: var(--paper);
  }
  .contact-line {
    position: absolute; left: 0; right: 0; top: 638px;
    display: flex; justify-content: center; gap: 16px;
    font-size: 19px; color: var(--text-dark);
  }
  .contact-line span { display: flex; align-items: center; gap: 8px; }
  .contact-line svg { width: 16px; height: 16px; }
  .credentials {
    position: absolute; left: 0; right: 0; top: 675px;
    display: flex; justify-content: center; align-items: center; gap: 16px;
  }
  .badge-certified { width: 87px; height: 25px; background: var(--badge-red); border-radius: 2px; }
  .badge-rating { width: 20px; height: 33px; background: var(--badge-blue); }
  .social-band {
    position: absolute; left: 0; bottom: 0; width: 100%; height: 57px;
    background: var(--teal);
    display: flex; justify-content: center; align-items: center; gap: 13px;
  }
  .social-dot { width: 32px; height: 32px; border: 2px solid var(--paper); border-radius: 50%; }
</style>
</head>
<body>
  <main class="yard-sign">
    <svg class="roof-header" viewBox="0 0 585 215" aria-hidden="true">
      <defs>
        <linearGradient id="roofShade" x1="0" y1="0" x2="1" y2="0">
          <stop offset="0" stop-color="#2a2a2a" stop-opacity="0"/>
          <stop offset="1" stop-color="#3a3a3a"/>
        </linearGradient>
      </defs>
      <rect width="585" height="215" fill="var(--ink)"/>
      <polygon points="330,141 585,95 585,212" fill="url(#roofShade)"/>
      <polygon points="0,212 330,141 585,212 585,215 0,215" fill="var(--paper)"/>
    </svg>
    <div class="brand">
      <span class="brand-mark"></span>
      <span class="brand-name">Qb Dale Outworks</span>
    </div>

    <h1 class="title-small">New Roof</h1>
    <h2 class="title-large">IN PROGRESS</h2>

    <div class="services-band"><span>S</span><span>E</span><span>R</span><span>V</span><span>I</span><span>C</span><span>E</span><span>S</span></div>

    <ul class="service-list row-one">
      <li><svg viewBox="0 0 17 17"><rect x="1" y="1" width="15" height="15" fill="none" stroke="var(--teal)" stroke-width="1.6"/><path d="M4 9l3 3 6-7" fill="none" stroke="var(--teal)" stroke-width="2"/></svg>Roofing</li>
      <li><svg viewBox="0 0 17 17"><rect x="1" y="1" width="15" height="15" fill="none" stroke="var(--teal)" stroke-width="1.6"/><path d="M4 9l3 3 6-7" fill="none" stroke="var(--teal)" stroke-width="2"/></svg>Gutters</li>
      <li><svg viewBox="0 0 17 17"><rect x="1" y="1" width="15" height="15" fill="none" stroke="var(--teal)" stroke-width="1.6"/><path d="M4 9l3 3 6-7" fill="none" stroke="var(--teal)" stroke-width="2"/></svg>Painting</li>
    </ul>
    <ul class="service-list row-two">
      <li><svg viewBox="0 0 17 17"><rect x="1" y="1" width="15" height="15" fill="none" stroke="var(--teal)" stroke-width="1.6"/><path d="M4 9l3 3 6-7" fill="none" stroke="var(--teal)" stroke-width="2"/></svg>Pressure Washing</li>
      <li><svg viewBox="0 0 17 17"><rect x="1" y="1" width="15" height="15" fill="none" stroke="var(--teal)" stroke-width="1.6"/><path d="M4 9l3 3 6-7" fill="none" stroke="var(--teal)" stroke-width="2"/></svg>Exterior Design</li>
    </ul>

    <svg class="phone-banner" viewBox="0 0 553 80" aria-hidden="true">
      <polygon points="0,40 40,0 513,0 553,40 513,80 40,80" fill="var(--charcoal)"/>
      <circle cx="78" cy="40" r="24" fill="none" stroke="var(--paper)" stroke-width="4"/>
      <path d="M68 29c2-2 4-2 5 0l3 5c1 2 0 3-1 4l-2 1c1 3 4 6 7 7l1-2c1-1 2-2 4-1l5 3c2 1 2 3 0 5l-3 3c-9 1-22-12-21-21z" fill="var(--paper)"/>
    </svg>
    <div class="phone-number">(555) 274-0198</div>

    <div class="contact-line">
      <span><svg viewBox="0 0 16 16"><rect x="1" y="3" width="14" height="10" fill="none" stroke="var(--teal)" stroke-width="1.4"/><path d="M1 3l7 6 7-6" fill="none" stroke="var(--teal)" stroke-width="1.4"/></svg>info@qbdaleoutworks.com</span>
      <span><svg viewBox="0 0 16 16"><circle cx="8" cy="8" r="7" fill="none" stroke="var(--teal)" stroke-width="1.3"/><ellipse cx="8" cy="8" rx="3" ry="7" fill="none" stroke="var(--teal)" stroke-width="1.1"/><path d="M1 8h14" stroke="var(--teal)" stroke-width="1.1"/></svg>www.qbdaleoutworks.com</span>
    </div>

    <div class="credentials">
      <span class="badge-certified" role="img" aria-label="Roofing manufacturer certification badge"></span>
      <span class="badge-rating" role="img" aria-label="Business accreditation badge"></span>
    </div>

    <footer class="social-band" aria-label="Social media links">
      <span class="social-dot"></span><span class="social-dot"></span><span class="social-dot"></span><span class="social-dot"></span>
      <span class="social-dot"></span><span class="social-dot"></span><span class="social-dot"></span><span class="social-dot"></span>
    </footer>
  </main>
</body>
</html>
```